New look while maintaining the Brand identification!

I want a new look for my business card. I want to keep the same colors and feel but change the look and layout a bit. The logo (KINOVALEX Physical therapy Reimagined and the lilypad) must remain the same and in that font.
We are a physical therapy clinic. So we have certification that we can write on the back or services we provide (which is what we currently have on the back of the card as well)

Contact information
2846 Cedar Hollow Rd., #22
Naples, FL 34187
P: (239) 555-0172
F: (239) 555-0198
E: kinovalextherapy@example-mail.com
W: www.kinovalextherapy-example.com

Industry/Entity Type

Physical Therapy

Contact Information for Business Card

Our current cards have the business address and information on the back. But I am willing to have it be in the front.

Font styles to use
Sans Serif

Colors
abd036
fbf289
ec1f27

Requirements
Must have
• Has to be unique!
• Services we provide and/or techniques we do must fit on the card
Nice to have
• Would like to have the front and back somehow linked together. Such that if you set the front next to the back, there is a nice flow of design! Currently the back is white with writing on it.
Should not have
• I like the wave lines as compared to straight lines.

```html
<!DOCTYPE html>
<html lang="en">
<head>
<meta charset="UTF-8">
<title>Kinovalex Business Card</title>
<link rel="stylesheet" href="https://fonts.googleapis.com/css2?family=Oswald:wght@500;600&family=Nunito+Sans:wght@400&family=Delius&display=swap">
<style>
  :root {
    --stage: #ebe7dc;
    --olive: #8e9a35;
    --meadow: #d8cc55;
    --gold: #d2b62c;
    --white: #ffffff;
    --alert-red: #e0452a;
    --ink: #3f3f3a;
    --ink-soft: #55544c;
  }
  * { margin: 0; padding: 0; box-sizing: border-box; }
  html, body { width: 1200px; height: 843px; overflow: hidden; }
  body { background: var(--stage); position: relative; font-family: "Nunito Sans", sans-serif; }

  .card {
    position: absolute;
    top: 252px;
    width: 557px;
    height: 318px;
    overflow: hidden;
    background: var(--white);
    box-shadow: 0 4px 12px rgba(0,0,0,0.25);
  }
  .card--front { left: 29px; }
  .card--back { left: 614px; }
  .card__waves { position: absolute; inset: 0; width: 100%; height: 100%; }

  .brand-name {
    position: absolute;
    font-family: "Oswald", sans-serif;
    font-weight: 600;
    font-size: 58px;
    line-height: 1;
    letter-spacing: 1px;
    color: var(--gold);
  }
  .card--front .brand-name { right: 26px; top: 60px; }
  .card--back .brand-name { left: 29px; top: 64px; }

  .holder { position: absolute; left: 24px; top: 151px; }
  .holder__name {
    font-family: "Oswald", sans-serif;
    font-weight: 500;
    font-size: 19px;
    color: var(--alert-red);
    line-height: 1.1;
  }
  .holder__name .credentials {
    font-family: "Nunito Sans", sans-serif;
    font-size: 13px;
    border-left: 2px solid var(--alert-red);
    padding-left: 4px;
    margin-left: 2px;
  }
  .holder__certs { margin-top: 3px; font-size: 13px; line-height: 18px; color: var(--ink-soft); }

  .contact-list { position: absolute; left: 27px; top: 219px; list-style: none; }
  .contact-list li {
    display: flex; align-items: center; gap: 8px;
    height: 21px; font-size: 13.5px; color: var(--ink);
  }
  .contact-list svg { width: 11px; height: 11px; fill: var(--alert-red); flex: none; }

  .address {
    position: absolute; right: 26px; top: 262px;
    text-align: right; font-size: 13.5px; line-height: 18px; color: var(--ink);
  }

  .tagline {
    position: absolute; left: 111px; top: 200px;
    font-family: "Delius", sans-serif;
    font-size: 25px; color: var(--ink);
    white-space: nowrap;
  }
  .tagline .accent { color: var(--alert-red); }
</style>
</head>
<body>

<section class="card card--front">
  <svg class="card__waves" viewBox="0 0 661 377" preserveAspectRatio="none" aria-hidden="true">
    <path d="M0,0 H661 V10 C520,4 300,28 0,88 Z" fill="var(--olive)"/>
    <path d="M0,96 C300,36 520,14 661,18" fill="none" stroke="var(--meadow)" stroke-width="4"/>
    <path d="M0,124 C180,104 360,196 661,206" fill="none" stroke="var(--meadow)" stroke-width="4"/>
    <path d="M0,132 C180,114 360,204 661,216 V377 H0 Z" fill="var(--meadow)"/>
  </svg>

  <div class="brand-name">KINOVALEX</div>

  <div class="holder">
    <p class="holder__name">DANA MERROW <span class="credentials">PT, DPT, MSPT, MBA</span></p>
    <p class="holder__certs">Certified Schroth Scoliosis Therapist.<br>Certified Equine Rehab Specialist. CAPP-OB</p>
  </div>

  <ul class="contact-list">
    <li>
      <svg viewBox="0 0 12 12"><path d="M2.5 0.5 L4.5 3 L3.4 4.3 C4.2 6 5.8 7.6 7.6 8.5 L8.9 7.4 L11.5 9.4 L10 11.5 C5.5 11 1 6.5 0.5 2 Z"/></svg>
      (239) 555-0172
    </li>
    <li>
      <svg viewBox="0 0 12 12"><rect x="3" y="0.5" width="6" height="3"/><rect x="0.5" y="4" width="11" height="5" rx="1"/><rect x="3" y="8" width="6" height="3.5"/></svg>
      (239) 555-0198
    </li>
    <li>
      <svg viewBox="0 0 12 12"><path d="M0.5 2 H11.5 V10 H0.5 Z M1.5 3 L6 6.5 L10.5 3 Z" fill-rule="evenodd"/></svg>
      kinovalextherapy@example-mail.com
    </li>
    <li>
      <svg viewBox="0 0 12 12"><path d="M6 0.5 A5.5 5.5 0 1 0 6 11.5 A5.5 5.5 0 1 0 6 0.5 Z M6 1.7 A4.3 4.3 0 1 1 6 10.3 A4.3 4.3 0 1 1 6 1.7 Z"/><path d="M1 5.5 H11 V6.5 H1 Z M5.5 1 H6.5 V11 H5.5 Z"/></svg>
      www.kinovalextherapy-example.com
    </li>
  </ul>

  <p class="address">2846 Cedar Hollow Rd., #22<br>Naples, FL 34187</p>
</section>

<section class="card card--back">
  <svg class="card__waves" viewBox="0 0 661 377" preserveAspectRatio="none" aria-hidden="true">
    <path d="M0,0 H661 V88 C360,28 140,4 0,10 Z" fill="var(--olive)"/>
    <path d="M0,18 C140,14 360,36 661,96" fill="none" stroke="var(--meadow)" stroke-width="4"/>
    <path d="M0,206 C300,196 480,104 661,124" fill="none" stroke="var(--meadow)" stroke-width="4"/>
    <path d="M0,216 C300,204 480,114 661,132 V377 H0 Z" fill="var(--meadow)"/>
  </svg>

  <div class="brand-name">KINOVALEX</div>

  <p class="tagline">Physical Therapy <span class="accent">Reimagined</span></p>
</section>

</body>
</html>
```